Stationery Design Project

We need a stationery design for a new business consulting business based in New Zealand.
We have the logo and business cards designed and we're looking for letterhead, compliments slip and PowerPoint presentation format that aligns with our business cards.
Industry/Entity Type
Business
Requirements
Must have
- same colors and format as business cards

```html
<!DOCTYPE html>
<html lang="en">
<head>
<meta charset="utf-8">
<title>Kauri Advisory – Stationery</title>
<link rel="stylesheet" href="https://fonts.googleapis.com/css2?family=Didact+Gothic&family=Open+Sans:wght@700;800&display=swap">
<style>
  :root {
    --backdrop: #e4e4e2;
    --paper: #ffffff;
    --brand-green: #8cc63f;
    --brand-grey: #9a9a9a;
    --text-grey: #8a8a8a;
    --edge-shadow: rgba(0, 0, 0, 0.28);
  }
  html, body {
    margin: 0;
    padding: 0;
    width: 1200px;
    height: 849px;
    overflow: hidden;
    background: var(--backdrop);
  }
  .sheet {
    position: absolute;
    background: var(--paper);
    box-shadow: 4px 5px 10px var(--edge-shadow);
  }
  .letterhead { left: 65px; top: 25px; width: 617px; height: 797px; }
  .compliments-slip { left: 536px; top: 437px; width: 600px; height: 281px; }

  .accent-bar { position: absolute; background: var(--brand-green); top: 0; right: 0; }
  .letterhead .accent-bar { width: 320px; height: 13px; }
  .compliments-slip .accent-bar { width: 141px; height: 12px; }

  .side-bar { position: absolute; left: 0; bottom: 0; width: 13px; background: var(--brand-grey); }
  .letterhead .side-bar { height: 319px; }
  .compliments-slip .side-bar { height: 140px; }

  .brand-name {
    position: absolute;
    margin: 0;
    font-family: "Didact Gothic", sans-serif;
    font-weight: 400;
    color: var(--brand-grey);
    letter-spacing: -0.5px;
    white-space: nowrap;
    line-height: 1;
  }
  .letterhead .brand-name { left: 38px; top: 40px; font-size: 37px; }
  .compliments-slip .brand-name { left: 30px; top: 29px; font-size: 31px; }

  .slip-title {
    position: absolute;
    left: 30px; top: 122px;
    margin: 0;
    font-family: "Open Sans", sans-serif;
    font-weight: 800;
    font-size: 19px;
    color: var(--brand-green);
  }

  .contact {
    position: absolute;
    display: flex;
    font-family: "Open Sans", sans-serif;
    font-weight: 700;
    font-size: 8px;
    line-height: 10.5px;
    color: var(--text-grey);
  }
  .letterhead .contact { left: 297px; top: 747px; }
  .compliments-slip .contact { left: 30px; top: 246px; }
  .contact address { font-style: normal; width: 138px; }
  .contact ul { list-style: none; margin: 0; padding: 0; }
  .contact li { display: flex; align-items: center; gap: 4px; }
  .contact svg { width: 8px; height: 8px; flex: none; }
</style>
</head>
<body>

<section class="sheet letterhead">
  <div class="accent-bar"></div>
  <h1 class="brand-name">Kauri Advisory</h1>
  <footer class="contact">
    <address>PO Box 48 170<br>Napier 4140 New Zealand</address>
    <ul>
      <li><svg viewBox="0 0 8 8"><rect x="0.5" y="1.5" width="7" height="5" fill="none" stroke="#8cc63f"/><path d="M0.5 1.5 4 4.5 7.5 1.5" fill="none" stroke="#8cc63f"/></svg>hello@kauriadvisory.co.nz</li>
      <li><svg viewBox="0 0 8 8"><circle cx="4" cy="4" r="3.5" fill="#8cc63f"/><path d="M0.5 4h7M4 0.5c-2 2-2 5 0 7M4 0.5c2 2 2 5 0 7" fill="none" stroke="#fff" stroke-width="0.6"/></svg>www.kauriadvisory.co.nz</li>
    </ul>
  </footer>
  <div class="side-bar"></div>
</section>

<section class="sheet compliments-slip">
  <div class="accent-bar"></div>
  <h1 class="brand-name">Kauri Advisory</h1>
  <h2 class="slip-title">With Compliments</h2>
  <footer class="contact">
    <address>PO Box 48 170<br>Napier 4140 New Zealand</address>
    <ul>
      <li><svg viewBox="0 0 8 8"><rect x="0.5" y="1.5" width="7" height="5" fill="none" stroke="#8cc63f"/><path d="M0.5 1.5 4 4.5 7.5 1.5" fill="none" stroke="#8cc63f"/></svg>hello@kauriadvisory.co.nz</li>
      <li><svg viewBox="0 0 8 8"><circle cx="4" cy="4" r="3.5" fill="#8cc63f"/><path d="M0.5 4h7M4 0.5c-2 2-2 5 0 7M4 0.5c2 2 2 5 0 7" fill="none" stroke="#fff" stroke-width="0.6"/></svg>www.kauriadvisory.co.nz</li>
    </ul>
  </footer>
  <div class="side-bar"></div>
</section>

</body>
</html>
```